Design me a minimalist business card

I need a minimalist, one-sided business card with name, email, phone number, location (university)

I am leaning towards a dark theme, but open to other ideas. Will probably print on matte paper with metallic text.

```html
<!DOCTYPE html>
<html lang="en">
<head>
<meta charset="UTF-8">
<title>Business Card – Daniel Marsh</title>
<link rel="stylesheet" href="https://fonts.googleapis.com/css2?family=Open+Sans:wght@400;700&display=swap">
<style>
  :root {
    --canvas-bg: #2a2a2a;
    --card-black: #050505;
    --band-grey: #4b4b4b;
    --text-white: #f2f2f2;
    --text-soft: #c9c9c9;
    --icon-line: #e6e6e6;
  }
  * { margin: 0; padding: 0; box-sizing: border-box; }
  html, body {
    width: 1200px;
    height: 836px;
    overflow: hidden;
    background: var(--canvas-bg);
    font-family: "Open Sans", sans-serif;
  }
  .canvas {
    position: relative;
    width: 1200px;
    height: 836px;
    display: flex;
    align-items: center;
    justify-content: center;
  }
  .business-card {
    position: relative;
    width: 900px;
    height: 514px;
    background: var(--card-black);
    border-radius: 22px;
    overflow: hidden;
    color: var(--text-white);
  }
  .identity {
    position: absolute;
    left: 64px;
    top: 52px;
  }
  .identity__name {
    font-size: 50px;
    font-weight: 700;
    line-height: 1.05;
    letter-spacing: 0.2px;
  }
  .identity__role {
    font-size: 22px;
    font-weight: 400;
    color: var(--text-soft);
    margin-top: 4px;
  }
  .contact-list {
    position: absolute;
    left: 64px;
    top: 196px;
    list-style: none;
  }
  .contact-item {
    display: flex;
    align-items: center;
    gap: 22px;
    height: 58px;
    margin-bottom: 14px;
    font-size: 24px;
  }
  .contact-item__icon {
    width: 50px;
    height: 50px;
    flex: none;
  }
  .address-band {
    position: absolute;
    left: 0;
    right: 0;
    bottom: 0;
    height: 74px;
    background: var(--band-grey);
    display: flex;
    align-items: center;
    justify-content: center;
    font-size: 24px;
    color: var(--text-white);
  }
  .address-band__label { font-weight: 700; margin-right: 6px; }
</style>
</head>
<body>
<main class="canvas">
  <section class="business-card" aria-label="Business card">
    <header class="identity">
      <h1 class="identity__name">Daniel Marsh</h1>
      <p class="identity__role">Teacher</p>
    </header>

    <ul class="contact-list">
      <li class="contact-item">
        <svg class="contact-item__icon" viewBox="0 0 50 50" aria-hidden="true">
          <rect x="1.5" y="1.5" width="47" height="47" fill="none" stroke="var(--icon-line)" stroke-width="2"/>
          <rect x="17" y="10" width="16" height="30" rx="2.5" fill="none" stroke="var(--icon-line)" stroke-width="2"/>
          <line x1="17" y1="15" x2="33" y2="15" stroke="var(--icon-line)" stroke-width="1.6"/>
          <line x1="17" y1="34" x2="33" y2="34" stroke="var(--icon-line)" stroke-width="1.6"/>
          <circle cx="25" cy="37" r="1.3" fill="var(--icon-line)"/>
        </svg>
        <span class="contact-item__text">555 210 347</span>
      </li>
      <li class="contact-item">
        <svg class="contact-item__icon" viewBox="0 0 50 50" aria-hidden="true">
          <rect x="1.5" y="1.5" width="47" height="47" fill="none" stroke="var(--icon-line)" stroke-width="2"/>
          <rect x="10" y="15" width="30" height="20" fill="none" stroke="var(--icon-line)" stroke-width="2"/>
          <polyline points="10,15 25,27 40,15" fill="none" stroke="var(--icon-line)" stroke-width="2" stroke-linejoin="round"/>
        </svg>
        <span class="contact-item__text">hello@danielmarsh.com</span>
      </li>
    </ul>

    <footer class="address-band">
      <span class="address-band__label">Address:</span>
      <span class="address-band__value">Your University location</span>
    </footer>
  </section>
</main>
</body>
</html>
```